logo & Business Card Design

BrightHaven Termite & Pest Control, I need a great logo, take my ideas and run with them!
I will use this in marketing and website so needs to be eye catching but professional

Target Market(s)

Resedintial & Business

Industry/Entity Type

Marketing

Contact Information for Business Card

Need front side with pertinent info & Logo; back side will have a 25% off initial services Coupon!

Font styles to use
Sans Serif

Colors
ec1f27
1b1b1b

Requirements
Must have
• Professional logo and style
Nice to have
• Raised lettering, black, red, white colors maybe? I'm flexible, but those colors go good on any background, vehicle, uniform, etc...
Should not have
• Cheesy

```html
<!DOCTYPE html>
<html lang="en">
<head>
<meta charset="utf-8">
<title>BrightHaven Termite &amp; Pest Control – Business Card</title>
<link rel="stylesheet" href="https://fonts.googleapis.com/css2?family=Montserrat:wght@300;400;600;700&display=swap">
<style>
  :root {
    --red: #ec1f27;
    --red-deep: #8e0f1c;
    --red-mid: #c21a2e;
    --ink: #1b1b1b;
    --black: #0c0c0c;
    --white: #ffffff;
    --silver: #b9b9b9;
    --silver-dark: #6d6d6d;
    --page: #ececec;
  }
  * { box-sizing: border-box; margin: 0; padding: 0; }
  html, body { width: 1200px; height: 1000px; overflow: hidden; }
  body {
    background: var(--page);
    font-family: "Montserrat", sans-serif;
    color: var(--white);
    position: relative;
  }
  .card {
    position: absolute;
    left: 250px;
    width: 700px;
    height: 400px;
    border-radius: 26px;
    overflow: hidden;
    box-shadow: 0 14px 30px rgba(0,0,0,.28);
  }

  /* Front */
  .card-front { top: 50px; background: radial-gradient(circle at 45% 30%, #2e2e2e, var(--black) 70%); }
  .brand { position: absolute; left: 200px; top: 48px; display: flex; align-items: center; gap: 16px; }
  .brand-dot { width: 58px; height: 58px; border-radius: 50%; background: var(--red); flex: none; }
  .brand-name { font-weight: 700; font-size: 46px; line-height: 1; letter-spacing: -0.5px; color: var(--white); white-space: nowrap; }
  .brand-sub { font-weight: 300; font-size: 22px; margin-top: 4px; color: var(--white); white-space: nowrap; }
  .tag-band {
    position: absolute; left: 0; right: 0; top: 178px; height: 30px;
    background: linear-gradient(90deg, var(--silver-dark), var(--silver) 40%, #e5e5e5 60%, var(--silver-dark));
    color: var(--ink); font-size: 15px; letter-spacing: 1px;
    display: flex; align-items: center; justify-content: center;
    white-space: nowrap;
  }
  .red-panel {
    position: absolute; left: 0; right: 0; top: 208px; bottom: 0;
    background: radial-gradient(ellipse at 50% 35%, var(--red-mid), var(--red-deep) 75%);
  }
  .person { position: absolute; left: 60px; top: 80px; text-align: right; }
  .person-name { font-weight: 700; font-size: 24px; white-space: nowrap; }
  .person-role { font-weight: 300; font-size: 22px; margin-top: 2px; }
  .contacts { position: absolute; left: 310px; top: 40px; list-style: none; }
  .contacts li { display: flex; align-items: center; gap: 12px; font-size: 18px; font-weight: 400; margin-bottom: 10px; white-space: nowrap; }
  .contacts svg { width: 24px; height: 24px; flex: none; }

  /* Back */
  .card-back { top: 520px; background: radial-gradient(circle at 40% 35%, #2c2c2c, var(--black) 70%); }
  .corner-accent { position: absolute; right: -70px; top: -90px; width: 260px; height: 260px; }
  .back-brand { position: absolute; left: 70px; top: 60px; }
  .back-brand .brand-name { font-size: 44px; }
  .back-brand .brand-sub { font-size: 22px; }
  .offer { position: absolute; left: 70px; top: 140px; display: flex; align-items: flex-start; }
  .offer-number { font-weight: 600; font-size: 170px; line-height: 1; letter-spacing: -4px; }
  .offer-unit { margin-left: 14px; margin-top: 6px; }
  .offer-percent { font-weight: 300; font-size: 80px; line-height: 1; }
  .offer-off { font-weight: 300; font-size: 52px; line-height: 1; color: var(--red); }
  .offer-note { position: absolute; left: 70px; top: 326px; font-weight: 600; font-size: 30px; letter-spacing: 0.5px; white-space: nowrap; }
</style>
</head>
<body>

<section class="card card-front" aria-label="Business card front">
  <div class="brand">
    <span class="brand-dot"></span>
    <div>
      <div class="brand-name">BrightHaven</div>
      <div class="brand-sub">Termite &amp; Pest Control</div>
    </div>
  </div>
  <div class="tag-band">Trusted, lasting care for your home or business</div>
  <div class="red-panel">
    <div class="person">
      <div class="person-name">Daniel Brooks</div>
      <div class="person-role">President</div>
    </div>
    <ul class="contacts">
      <li>
        <svg viewBox="0 0 24 24"><circle cx="12" cy="12" r="11" fill="#fff"/><rect x="8" y="5" width="8" height="14" rx="1.5" fill="none" stroke="#8e0f1c" stroke-width="1.8"/><line x1="11" y1="16.5" x2="13" y2="16.5" stroke="#8e0f1c" stroke-width="1.6"/></svg>
        555-014-2290
      </li>
      <li>
        <svg viewBox="0 0 24 24"><circle cx="12" cy="12" r="11" fill="#fff"/><rect x="6" y="8" width="12" height="8" fill="none" stroke="#8e0f1c" stroke-width="1.6"/><polyline points="6,8 12,13 18,8" fill="none" stroke="#8e0f1c" stroke-width="1.6"/></svg>
        dan@brighthavenpest.com
      </li>
      <li>
        <svg viewBox="0 0 24 24"><circle cx="12" cy="12" r="11" fill="#fff"/><circle cx="12" cy="12" r="6" fill="none" stroke="#8e0f1c" stroke-width="1.5"/><ellipse cx="12" cy="12" rx="2.6" ry="6" fill="none" stroke="#8e0f1c" stroke-width="1.3"/><line x1="6" y1="12" x2="18" y2="12" stroke="#8e0f1c" stroke-width="1.3"/></svg>
        www.brighthavenpestcontrol.com
      </li>
    </ul>
  </div>
</section>

<section class="card card-back" aria-label="Business card back, new customer coupon">
  <svg class="corner-accent" viewBox="0 0 260 260" aria-hidden="true">
    <circle cx="130" cy="130" r="124" fill="#c21a2e" stroke="#fff" stroke-width="10"/>
  </svg>
  <div class="back-brand">
    <div class="brand-name">BrightHaven</div>
    <div class="brand-sub">Termite &amp; Pest Control</div>
  </div>
  <div class="offer">
    <div class="offer-number">25</div>
    <div class="offer-unit">
      <div class="offer-percent">%</div>
      <div class="offer-off">off</div>
    </div>
  </div>
  <div class="offer-note">FOR NEW CUSTOMERS</div>
</section>

</body>
</html>
```